Design a double sided business card

We are looking for a clean, eye-catching, and contemporary design that enhances the brand and presents a premium, professional image. Our preference is for a brown card with black gloss detailing and embossed elements; however, we are open to creative input and design suggestions that best achieve a strong visual impact.

Please see the attached existing business card for reference. We use both black and brown colours consistently across our branding.

On sample provided

```html
<!DOCTYPE html>
<html lang="en">
<head>
<meta charset="utf-8">
<title>Halvorn – Business Card</title>
<link rel="stylesheet" href="https://fonts.googleapis.com/css2?family=Syncopate:wght@700&family=Poppins:wght@400;600&display=swap">
<style>
  :root {
    --page: #e8eaea;
    --black: #0b0b0b;
    --sand: #d8c5a8;
    --grey: #8f8f8f;
    --ink: #111111;
  }
  * { box-sizing: border-box; margin: 0; padding: 0; }
  html, body {
    width: 1200px; height: 900px; overflow: hidden;
    background: var(--page);
  }
  .sheet {
    width: 1200px; height: 900px;
    display: flex; flex-direction: column;
    align-items: center; justify-content: center; gap: 36px;
  }
  .card {
    position: relative; width: 700px; height: 400px;
    box-shadow: 0 6px 18px rgba(0,0,0,.18);
  }
  .card-frame { position: absolute; inset: 0; width: 700px; height: 400px; }
  .card-content { position: absolute; inset: 0; }

  /* Front */
  .front-lockup {
    position: absolute; inset: 0;
    display: flex; align-items: center; justify-content: center; gap: 26px;
  }
  .lockup-square {
    width: 66px; height: 66px; border: 5px solid var(--sand);
  }
  .lockup-rule { width: 2px; height: 84px; background: var(--sand); }
  .front-wordmark {
    font-family: "Syncopate", sans-serif; font-weight: 700;
    font-size: 50px; letter-spacing: 4px; color: var(--sand);
  }

  /* Back */
  .back-main {
    position: absolute; left: 80px; right: 70px; top: 120px;
    display: flex; align-items: center; gap: 22px;
  }
  .identity { text-align: right; }
  .back-wordmark {
    font-family: "Syncopate", sans-serif; font-weight: 700;
    font-size: 40px; letter-spacing: 3px; color: var(--ink); line-height: 1;
  }
  .person { margin-top: 22px; font-family: "Poppins", sans-serif; color: var(--ink); }
  .person-name { font-weight: 600; font-size: 17px; letter-spacing: .5px; line-height: 1.1; }
  .person-role { font-size: 12px; line-height: 1.1; }
  .back-rule { width: 1.5px; height: 118px; background: var(--ink); align-self: center; }
  .contacts { list-style: none; font-family: "Poppins", sans-serif; font-size: 13px; color: var(--ink); }
  .contacts li { display: flex; align-items: center; gap: 8px; line-height: 22px; }
  .contacts svg { width: 14px; height: 14px; flex: none; }
  .address {
    position: absolute; left: 0; right: 0; bottom: 70px; text-align: center;
    font-family: "Poppins", sans-serif; font-size: 13px; color: var(--ink);
  }
</style>
</head>
<body>
<main class="sheet">

  <section class="card card-front" aria-label="Card front">
    <svg class="card-frame" viewBox="0 0 700 400" aria-hidden="true">
      <rect width="700" height="400" fill="var(--sand)"/>
      <rect x="40" y="40" width="620" height="320" fill="var(--black)"/>
      <polygon points="580,0 700,0 700,150 660,110 660,40 620,40" fill="var(--grey)"/>
      <polygon points="580,400 700,400 700,250 660,290 660,360 620,360" fill="var(--grey)"/>
      <line x1="580" y1="0" x2="620" y2="40" stroke="var(--black)" stroke-width="3"/>
      <line x1="700" y1="150" x2="660" y2="110" stroke="var(--black)" stroke-width="3"/>
      <line x1="580" y1="400" x2="620" y2="360" stroke="var(--black)" stroke-width="3"/>
      <line x1="700" y1="250" x2="660" y2="290" stroke="var(--black)" stroke-width="3"/>
    </svg>
    <div class="card-content">
      <div class="front-lockup">
        <span class="lockup-square"></span>
        <span class="lockup-rule"></span>
        <span class="front-wordmark">HALVORN</span>
      </div>
    </div>
  </section>

  <section class="card card-back" aria-label="Card back">
    <svg class="card-frame" viewBox="0 0 700 400" aria-hidden="true">
      <rect width="700" height="400" fill="var(--black)"/>
      <rect x="40" y="40" width="620" height="320" fill="var(--sand)"/>
      <polygon points="120,0 0,0 0,150 40,110 40,40 80,40" fill="var(--grey)"/>
      <polygon points="120,400 0,400 0,250 40,290 40,360 80,360" fill="var(--grey)"/>
      <line x1="120" y1="0" x2="80" y2="40" stroke="var(--sand)" stroke-width="3"/>
      <line x1="0" y1="150" x2="40" y2="110" stroke="var(--sand)" stroke-width="3"/>
      <line x1="120" y1="400" x2="80" y2="360" stroke="var(--sand)" stroke-width="3"/>
      <line x1="0" y1="250" x2="40" y2="290" stroke="var(--sand)" stroke-width="3"/>
    </svg>
    <div class="card-content">
      <div class="back-main">
        <div class="identity">
          <div class="back-wordmark">HALVORN</div>
          <div class="person">
            <div class="person-name">RAJ KALER</div>
            <div class="person-role">Director</div>
          </div>
        </div>
        <span class="back-rule"></span>
        <ul class="contacts">
          <li>
            <svg viewBox="0 0 16 16" aria-hidden="true"><circle cx="8" cy="8" r="7" fill="none" stroke="currentColor" stroke-width="1.3"/><path d="M5.5 4.5l1.2 1.4-.7 1c.5 1 1.2 1.7 2.1 2.1l1-.7 1.4 1.2-.6 1.1c-2.6-.3-4.8-2.5-5-5z" fill="currentColor"/></svg>
            0800 555 0142
          </li>
          <li>
            <svg viewBox="0 0 16 16" aria-hidden="true"><circle cx="8" cy="8" r="7" fill="none" stroke="currentColor" stroke-width="1.3"/><rect x="5.7" y="4" width="4.6" height="8" rx="1" fill="none" stroke="currentColor" stroke-width="1.1"/></svg>
            07700900418
          </li>
          <li>
            <svg viewBox="0 0 16 16" aria-hidden="true"><circle cx="8" cy="8" r="7" fill="none" stroke="currentColor" stroke-width="1.3"/><rect x="4.5" y="5.5" width="7" height="5" fill="none" stroke="currentColor" stroke-width="1.1"/><path d="M4.5 5.5L8 8.3l3.5-2.8" fill="none" stroke="currentColor" stroke-width="1.1"/></svg>
            raj@halvorn.co.uk
          </li>
          <li>
            <svg viewBox="0 0 16 16" aria-hidden="true"><circle cx="8" cy="8" r="7" fill="none" stroke="currentColor" stroke-width="1.3"/><circle cx="8" cy="8" r="3.8" fill="none" stroke="currentColor" stroke-width="1"/><path d="M4.2 8h7.6M8 4.2v7.6" stroke="currentColor" stroke-width="1"/></svg>
            www.halvorn.co.uk
          </li>
        </ul>
      </div>
      <p class="address">12 Mill Meadow Lane, Eastbrook EB4 2QT</p>
    </div>
  </section>

</main>
</body>
</html>
```